Velmoro Cabinets Letter Head and Email Signature

Hi
I would love a design package for a letterhead, email signature, even update my business card if you like if you can come up with a great idea for my new high end cabinet shop. Velmoro Cabinets brings timeless craftsmanship to modern interiors, specializing in high end, custom cabinetry designed for architects and interior designers.

Target Market(s)

high end, luxury market

Industry/Entity Type

cabinet making

Requirements
Must have
• my colours of logo as the theme

```html
<!DOCTYPE html>
<html lang="en">
<head>
<meta charset="utf-8">
<title>Velmoro Cabinets Letterhead</title>
<link rel="stylesheet" href="https://fonts.googleapis.com/css2?family=Quicksand:wght@500&family=Tinos&family=Arimo&display=swap">
<style>
  :root {
    --ink: #0b0b0b;
    --brand-green: #4a7d4e;
    --paper: #ffffff;
    --backdrop: #b9b9b9;
    --body-text: #1a1a1a;
  }
  * { box-sizing: border-box; margin: 0; padding: 0; }
  html, body {
    width: 1200px; height: 1159px; overflow: hidden;
    background: var(--backdrop);
  }
  .letterhead {
    position: absolute; left: 200px; top: 14px;
    width: 800px; height: 1131px;
    background: var(--paper);
    box-shadow: 0 6px 24px rgba(0,0,0,.25);
    overflow: hidden;
  }
  .header {
    position: relative; height: 150px;
    background: var(--ink);
    border-bottom: 4px solid var(--brand-green);
    box-shadow: 0 4px 0 var(--ink);
  }
  .header::after {
    content: ""; position: absolute; left: 0; right: 0; bottom: -8px;
    height: 4px; background: var(--brand-green);
  }
  .brand {
    position: absolute; left: 60px; top: 52px;
    display: flex; align-items: center; gap: 14px;
  }
  .brand-mark { width: 14px; height: 14px; background: var(--brand-green); }
  .brand-name {
    font-family: "Quicksand", sans-serif; font-weight: 500;
    font-size: 38px; color: var(--brand-green); letter-spacing: 1px;
  }
  .contact {
    position: absolute; left: 500px; top: 22px; height: 110px;
    padding-left: 18px;
    border-left: 1px solid var(--brand-green);
    font-family: "Tinos", serif; font-size: 14px; line-height: 19px;
    color: var(--paper); list-style: none;
  }
  .contact li { display: flex; align-items: flex-start; gap: 10px; }
  .contact svg { width: 12px; height: 12px; margin-top: 4px; flex: none; fill: var(--brand-green); }
  .letter-body {
    padding: 150px 70px 0 210px;
    font-family: "Arimo", sans-serif; font-size: 13.5px; line-height: 16px;
    color: var(--body-text);
  }
  .letter-body p { margin-bottom: 32px; }
  .footer {
    position: absolute; left: 0; bottom: 0; width: 800px; height: 62px;
  }
</style>
</head>
<body>
<main class="letterhead">
  <header class="header">
    <div class="brand">
      <span class="brand-mark"></span>
      <span class="brand-name">Velmoro Cabinets</span>
    </div>
    <ul class="contact">
      <li><svg viewBox="0 0 12 12"><path d="M2 1l2 0 1 3-1.5 1a6 6 0 0 0 3.5 3.5L8 7l3 1v2a1 1 0 0 1-1 1A9 9 0 0 1 1 2a1 1 0 0 1 1-1z"/></svg>0491 570 156</li>
      <li><svg viewBox="0 0 12 12"><path d="M0 2h12v8H0zM1 3l5 4 5-4"/></svg>info@velmorocabinets.com.au</li>
      <li><svg viewBox="0 0 12 12"><circle cx="6" cy="6" r="5.5"/></svg>www.velmorocabinets.com.au</li>
      <li><svg viewBox="0 0 12 12"><path d="M6 0a4 4 0 0 1 4 4c0 3-4 8-4 8S2 7 2 4a4 4 0 0 1 4-4z"/></svg>18 Joinery Lane,<br>Brunswick VIC 3056</li>
    </ul>
  </header>

  <section class="letter-body">
    <p>Lorem ipsum dolor sit amet, consectetur adipiscing elit. Donec fringilla neque euismod volutpat cursus. Vestibulum ac pretium orci, consequat elementum velit. Etiam bibendum purus ac augue finibus volutpat. Vestibulum justo nisl.</p>
    <p>Lorem ipsum dolor sit amet, consectetur adipiscing elit. Donec fringilla neque euismod volutpat cursus. Vestibulum ac pretium orci, consequat elementum velit. Etiam bibendum purus ac augue finibus volutpat. Vestibulum justo nisl, gravida aliquet sollicitudin ut, finibus vitae mi. Praesent aliquet scelerisque blandit. Sed id varius lacus, id tristique sem. Fusce et lobortis leo. Aliquam mollis pellentesque magna, condimentum ullamcorper ex ullamcorper non. Morbi ultricies nunc eu tellus dignissim, eget venenatis dolor ullamcorper. Etiam dolor eros, iaculis at ultricies nec, volutpat nec orci. Vivamus tincidunt rutrum sapien, ac porttitor mauris tristique nec.</p>
    <p>Lorem ipsum dolor sit amet, consectetur adipiscing elit. Donec fringilla neque euismod volutpat cursus. Vestibulum ac pretium orci, consequat elementum velit. Etiam bibendum purus ac augue finibus volutpat. Vestibulum justo nisl, gravida aliquet sollicitudin ut, finibus vitae mi. Praesent aliquet scelerisque blandit. Sed id varius lacus, id tristique sem. Fusce et lobortis leo. Aliquam mollis pellentesque magna, condimentum ullamcorper ex ullamcorper non. Morbi ultricies nunc eu tellus dignissim, eget venenatis dolor ullamcorper. Etiam dolor eros, iaculis at ultricies nec, volutpat nec orci. Vivamus tincidunt rutrum sapien, ac porttitor mauris tristique nec.</p>
    <p>Lorem ipsum dolor sit amet, consectetur adipiscing elit. Donec fringilla neque euismod volutpat cursus. Vestibulum ac pretium orci, consequat elementum velit. Etiam bibendum purus ac augue finibus volutpat. Vestibulum justo nisl.</p>
  </section>

  <svg class="footer" viewBox="0 0 800 62" aria-hidden="true">
    <polygon points="0,28 505,28 530,62 0,62" fill="var(--ink)"/>
    <polygon points="500,0 800,0 800,62 545,62 515,22 500,22" fill="var(--brand-green)"/>
  </svg>
</main>
</body>
</html>
```